Letterhead Design for Law Firm that Specializes in Property Damage Litigation

We are looking for a redesign of our letterhead. Our current letterhead lists all of our current staff members and we'd like to come up with a design that does NOT list all of the staff members so that it does not need to be updated with every newly hired employee. Must be in editable format.

We are a law firm that specializes in property damage, so we need something that is professional, yet modern. The final design should use our existing logo and should use a blue color scheme (alternate colors would be gray, black, and white).

Industry/Entity Type

Legal

Colors
0054AA
0677BA
7BADD7
CADEEF
E8F1F8

```html
<!DOCTYPE html>
<html lang="en">
<head>
<meta charset="utf-8">
<title>Harlow Prentice &amp; Vale — Letterhead</title>
<link href="https://fonts.googleapis.com/css2?family=Cormorant+Garamond:wght@500;600&family=Nunito+Sans:wght@400;600&display=swap" rel="stylesheet">
<style>
  :root{
    --stage:#4f6580;
    --paper:#ffffff;
    --navy:#1b3468;
    --ink:#333a44;
    --gray:#6d6f73;
    --rule:#1b3468;
  }
  *{box-sizing:border-box;margin:0;padding:0}
  html,body{width:1200px;height:725px;overflow:hidden;background:var(--stage)}
  .letterhead{
    position:absolute;left:354px;top:30px;width:491px;height:665px;
    background:var(--paper);box-shadow:0 4px 14px rgba(0,0,0,.35);overflow:hidden;
    font-family:"Nunito Sans",Arial,sans-serif;color:var(--ink);
  }
  /* firm name */
  .firm{position:absolute;left:146px;top:24px;width:192px;text-align:center}
  .firm-name{
    font-family:"Cormorant Garamond",Georgia,serif;font-weight:600;
    font-size:22px;line-height:19px;letter-spacing:1.5px;color:var(--navy);
  }
  .firm-tagline{margin-top:12px;font-size:7.6px;letter-spacing:2.3px;color:var(--gray);white-space:nowrap}
  /* offices */
  .offices{position:absolute;left:362px;top:21px;width:120px}
  .office{margin-bottom:10px}
  .office-title{
    font-family:"Cormorant Garamond",Georgia,serif;font-weight:600;font-variant:small-caps;
    font-size:10.5px;letter-spacing:.6px;color:var(--navy);margin-bottom:3px;white-space:nowrap;
  }
  .contact{display:flex;align-items:flex-start;gap:5px;font-size:6.8px;line-height:8.8px;letter-spacing:.3px;margin-bottom:4.7px;color:var(--ink)}
  .contact svg{flex:none;width:9.5px;height:9.5px}
  .office-rule{width:35px;height:1px;background:var(--rule);margin:-1px 0 0 15px}
  .footer-wave{position:absolute;left:0;bottom:0;width:491px;height:50px}
</style>
</head>
<body>
<article class="letterhead">
  <header class="firm">
    <div class="firm-name">HARLOW<br>PRENTICE &amp;<br>VALE</div>
    <div class="firm-tagline">THE PROPERTY DAMAGE ATTORNEYS</div>
  </header>

  <section class="offices">
    <div class="office">
      <h2 class="office-title">Philadelphia Office</h2>
      <div class="contact"><svg viewBox="0 0 10 10"><circle cx="5" cy="5" r="5" fill="#1b3468"/><path d="M3.2 2.6l1 .1.4 1.2-.6.5a3.5 3.5 0 0 0 1.6 1.6l.5-.6 1.2.4.1 1c-2.5.3-4.5-1.7-4.2-4.2z" fill="#fff"/></svg>215.555.0140</div>
      <div class="contact"><svg viewBox="0 0 10 10"><circle cx="5" cy="5" r="5" fill="#1b3468"/><rect x="2.6" y="3" width="4.8" height="4.2" rx=".5" fill="#fff"/><rect x="3.3" y="3.8" width="3.4" height="1" fill="#1b3468"/></svg>215.555.0187</div>
      <div class="contact"><svg viewBox="0 0 10 10"><circle cx="5" cy="5" r="5" fill="#1b3468"/><path d="M5 2a2 2 0 0 1 2 2c0 1.4-2 3.8-2 3.8S3 5.4 3 4a2 2 0 0 1 2-2z" fill="#fff"/><circle cx="5" cy="4" r=".7" fill="#1b3468"/></svg><span>2200 Market Street<br>Suite 840<br>Philadelphia, PA 19103</span></div>
      <div class="office-rule"></div>
    </div>
    <div class="office">
      <h2 class="office-title">New Jersey Office</h2>
      <div class="contact"><svg viewBox="0 0 10 10"><circle cx="5" cy="5" r="5" fill="#1b3468"/><path d="M3.2 2.6l1 .1.4 1.2-.6.5a3.5 3.5 0 0 0 1.6 1.6l.5-.6 1.2.4.1 1c-2.5.3-4.5-1.7-4.2-4.2z" fill="#fff"/></svg>856.555.0162</div>
      <div class="contact"><svg viewBox="0 0 10 10"><circle cx="5" cy="5" r="5" fill="#1b3468"/><rect x="2.6" y="3" width="4.8" height="4.2" rx=".5" fill="#fff"/><rect x="3.3" y="3.8" width="3.4" height="1" fill="#1b3468"/></svg>215.555.0187</div>
      <div class="contact"><svg viewBox="0 0 10 10"><circle cx="5" cy="5" r="5" fill="#1b3468"/><path d="M5 2a2 2 0 0 1 2 2c0 1.4-2 3.8-2 3.8S3 5.4 3 4a2 2 0 0 1 2-2z" fill="#fff"/><circle cx="5" cy="4" r=".7" fill="#1b3468"/></svg><span>480 Haddon Avenue<br>Suite 310<br>Cherry Hill, NJ 08034</span></div>
    </div>
  </section>

  <svg class="footer-wave" viewBox="0 0 491 50" preserveAspectRatio="none" aria-hidden="true">
    <path d="M0 2 C70 14 190 18 280 14 C360 10 430 0 491 16 L491 19 C430 4 360 13 280 17 C190 21 70 17 0 6 Z" fill="#6d6f73"/>
    <path d="M0 10 C80 22 200 24 290 18 C370 12 440 10 491 20 L491 50 L0 50 Z" fill="#1b3468"/>
  </svg>
</article>
</body>
</html>
```